| ■お仕事内容 海外の高級ファッションブランドを販売するサイト用の無償修理保証のバナー製作をお願いいたします。 メンズ、レディースどちらも取り扱っているブランドのため、どちらでも使えるデザインが望ましいです。 ■バナーに記載する内容 「1年間無償修理保証」ということが伝わる文章を入れてください。 ※独自のサービスのため、「当店だけの・・・」など独自の付加価値サービスである文言を入れたいです。 ■重視する点 ・高級感のあるデザイン(ごちゃごちゃしていない、シンプルで目を引くもの) ・フラットデザインが基調になっているサイトにマッチするデザイン ・ファッション系のサイトに合うデザイン ・本物である安心感・信頼感のあるデザイン ■報酬 5,000円 ■応募条件 WEBサイトのバナー、アイコンなどの製作経験をお持ちの方 ご提案価格と実績のバランスを見てお仕事をお願いする方を選定させていただきます。 たくさんのご応募お待ちしております。 何卒宜しくお願いいたします。 |

```html
<!DOCTYPE html>
<html lang="ja">
<head>
<meta charset="utf-8">
<title>1年間無償修理保証 バナー</title>
<link rel="stylesheet" href="https://fonts.googleapis.com/css2?family=Noto+Sans+JP:wght@700&family=Noto+Serif+JP:wght@900&display=swap">
<style>
  :root {
    --page-bg: #ffffff;
    --panel-dark: #141414;
    --panel-mid: #2b2b2b;
    --gold-deep: #6e5a2c;
    --gold-mid: #b89a5a;
    --gold-light: #f1e3b8;
    --ink-dark: #111111;
    --ink-light: #ffffff;
  }
  * { margin: 0; padding: 0; box-sizing: border-box; }
  html, body {
    width: 1200px;
    height: 412px;
    overflow: hidden;
    background: var(--page-bg);
  }
  .banner {
    position: relative;
    width: 1200px;
    height: 412px;
  }
  .banner-panel {
    position: absolute;
    left: 36px;
    top: 28px;
    width: 1128px;
    height: 352px;
    overflow: hidden;
  }
  .banner-shapes {
    position: absolute;
    inset: 0;
    width: 100%;
    height: 100%;
  }
  .banner-tagline {
    position: absolute;
    left: 0;
    right: 0;
    top: 26px;
    text-align: center;
    font-family: "Noto Sans JP", sans-serif;
    font-weight: 700;
    font-size: 40px;
    letter-spacing: 2px;
    color: var(--ink-dark);
    line-height: 1;
  }
  .banner-headline {
    position: absolute;
    left: 0;
    right: 0;
    top: 168px;
    text-align: center;
    font-family: "Noto Serif JP", serif;
    font-weight: 900;
    font-size: 100px;
    letter-spacing: 18px;
    color: var(--ink-light);
    line-height: 1;
    transform: skewX(-12deg);
  }
</style>
</head>
<body>
  <div class="banner">
    <div class="banner-panel">
      <svg class="banner-shapes" viewBox="0 0 1128 352" preserveAspectRatio="none" role="img" aria-label="黒い革のような質感の背景に金色の帯">
        <defs>
          <radialGradient id="dark-texture" cx="50%" cy="60%" r="70%">
            <stop offset="0" stop-color="var(--panel-mid)"/>
            <stop offset="1" stop-color="var(--panel-dark)"/>
          </radialGradient>
          <linearGradient id="gold-band" x1="0" y1="0" x2="1" y2="0">
            <stop offset="0" stop-color="var(--gold-deep)"/>
            <stop offset="0.45" stop-color="var(--gold-mid)"/>
            <stop offset="0.8" stop-color="var(--gold-light)"/>
            <stop offset="1" stop-color="var(--gold-mid)"/>
          </linearGradient>
        </defs>
        <rect class="dark-field" width="1128" height="352" fill="url(#dark-texture)"/>
        <path class="gold-field" d="M0 0 H1128 V122 C900 130 700 90 500 82 C300 74 140 86 0 96 Z" fill="url(#gold-band)"/>
        <path class="gold-edge" d="M0 96 C140 86 300 74 500 82 C700 90 900 130 1128 122" fill="none" stroke="var(--gold-light)" stroke-width="2" opacity="0.8"/>
      </svg>
      <p class="banner-tagline">当店だけの特別なサービス</p>
      <h1 class="banner-headline">1年間無償修理保証</h1>
    </div>
  </div>
</body>
</html>
```